Edit and changes to original promotional flyer

I have a promotional flyer designed for me but would like it changed. Some stuff added and some taken away and also for a fresh designer to put their mark on it.
I have the flyer in indesign file attached. I also have a lot of photos on our website/facebook. I have a new website which is about to be launched and I would like the flyer to run along the same lines.
Old website: hopscotchburrow.com
New website: http://hopscotchburrow.quillmoorstudio.co.uk/
Facebook: facebook.com/hopscotchburrow
I need to add in two new parties - Football party in our enclosed pitch taken by a professional football coach. The children will get receive some training and then get to play a game. The birthday child will also receive a leather football to take away! There will also be time for a play in the play area and you'll get your own party room for the party food and cake!
Also: NEW for 2016 (launching spring) Kids Bumper Cars! Book a bumper car party where you will get 30 minutes exclusive use of the bumper cars! The children will also get an hours play and half hour in their own party room for food and the cake celebration! (cake not included).
There is also more changes but as the file is in INDD I can't open it.
My old flyer is also attached. (green)
It needs to be the same format as the other brochures so tri-fold, double sided please.
Photos: https://files.vendrelbox.net/sc/q7wtmzpekr3vbn/ZQXpleodTnRuWc_k8y45fHsLe
PSD mascots: https://files.vendrelbox.net/sh/x3mvqb8tgk2jhy/ZQPwtrneuBmLkf_s9a4n2HcXo?dl=0
Target Market(s)
Mums - Dads - Grand parents and also children!
Industry/Entity Type
Promotional
Look and feel

```html
<!DOCTYPE html>
<html lang="en">
<head>
<meta charset="utf-8">
<title>Hopscotch Burrow Indoor Play – Trifold Inside</title>
<link rel="stylesheet" href="https://fonts.googleapis.com/css2?family=Chewy&family=Arimo:wght@400;700&display=swap">
<style>
  :root {
    --purple: #6150a3;
    --yellow: #fde100;
    --gold: #ffd800;
    --orange: #f7a823;
    --orange-soft: #f5b33e;
    --white: #ffffff;
    --heading-font: "Chewy", "Arial Narrow", Arial, sans-serif;
    --body-font: "Arimo", Arial, sans-serif;
  }
  * { margin: 0; padding: 0; box-sizing: border-box; }
  html, body { width: 1200px; height: 848px; overflow: hidden; background: var(--white); }
  .brochure { position: relative; width: 1200px; height: 848px; display: flex; }
  .panel { position: relative; height: 848px; overflow: hidden; }
  .panel--about { width: 400px; background: var(--purple); color: var(--white); }
  .panel--play { width: 401px; background: var(--yellow); color: var(--purple); }
  .panel--parties { width: 399px; background: var(--purple); color: var(--white); }

  .block { position: absolute; left: 20px; right: 19px; }
  .panel-title, .section-title, .subtitle {
    font-family: var(--heading-font); font-weight: 400; line-height: 1.1;
    white-space: nowrap;
  }
  .panel-title { font-size: 29px; text-align: center; }
  .section-title { font-size: 27px; letter-spacing: 0.2px; }
  .subtitle { font-size: 20px; }
  .subtitle--center { text-align: center; }
  .copy { font-family: var(--body-font); font-size: 15.8px; line-height: 20.7px; text-align: justify; }

  .panel--about .panel-title, .panel--about .section-title,
  .panel--parties .panel-title, .panel--parties .section-title { color: var(--gold); }
  .panel--about .subtitle, .panel--parties .subtitle { color: var(--orange); }
  .panel--play .panel-title, .panel--play .section-title { color: var(--purple); }
  .panel--play .subtitle { color: var(--orange-soft); }

  .about-title { top: 14px; }
  .about-sub { top: 56px; }
  .about-copy { top: 84px; }
  .children-title { top: 207px; }
  .physical-sub { top: 245px; }
  .physical-copy { top: 271px; }
  .mental-sub { top: 477px; }
  .mental-copy { top: 503px; }
  .adults-title { top: 626px; }
  .quality-sub { top: 664px; }
  .quality-copy { top: 691px; }

  .play-title { top: 15px; }
  .play-sub { top: 56px; }
  .play-copy { top: 84px; }
  .ice-title { top: 190px; }
  .ice-sub { top: 225px; }
  .ice-copy { top: 254px; }
  .juniors-title { top: 386px; }
  .juniors-sub { top: 424px; }
  .juniors-copy { top: 451px; }
  .toddlers-title { top: 582px; }
  .toddlers-sub { top: 621px; }
  .toddlers-copy { top: 647px; }
  .babies-title { top: 724px; }
  .babies-sub { top: 764px; }
  .babies-copy { top: 794px; }

  .parties-title { top: 14px; }
  .parties-sub { top: 56px; }
  .football-title { top: 100px; }
  .football-sub { top: 137px; }
  .football-copy { top: 164px; }
  .bumper-title { top: 420px; }
  .bumper-sub { top: 457px; }
  .bumper-copy { top: 484px; }
  .contact-copy { top: 700px; text-align: left; }
</style>
</head>
<body>
<main class="brochure">
  <section class="panel panel--about">
    <h1 class="block panel-title about-title">ABOUT US</h1>
    <h2 class="block subtitle subtitle--center about-sub">The Hopscotch Burrow Indoor Play</h2>
    <p class="block copy about-copy">A massive 20,000 square foot building packed to the rafters with fun and adventerous activities for children, whilst a welcoming, quality environment for parents to enjoy watching their children develop their skills at play.</p>

    <h2 class="block section-title children-title">KEEPING CHILDREN HAPPY</h2>
    <h3 class="block subtitle physical-sub">Physical Development</h3>
    <p class="block copy physical-copy">Hopscotch Burrow offers great play value to promote physical activity and encourage exercise in a controlled and safe environment. The play equipment is cleverly designed to encourage physical activities including - sliding, crawling, balancing, swinging, bouncing, squeezing, hand eye coordination, ball skills, etc, everything a developing child would expect to experience at play.</p>
    <h3 class="block subtitle mental-sub">Mental Development</h3>
    <p class="block copy mental-copy">Hopscotch Burrow offers play features to promote mental stimulation and intrigue with interactive light and sound features, interactive dwell areas, make belief activities, art and craft areas, dressing up, story time, social interaction</p>

    <h2 class="block section-title adults-title">KEEPING ADULTS HAPPY</h2>
    <h3 class="block subtitle quality-sub">Quality, clean, welcoming environment</h3>
    <p class="block copy quality-copy">With great food and beverage offering and importantly good line of sight to allow the parent to interact with their children or relax knowing their children are safe because they can see them at play.</p>
  </section>

  <section class="panel panel--play">
    <h1 class="block panel-title play-title">Play with us</h1>
    <h2 class="block subtitle subtitle--center play-sub">Fantastic activites for all ages</h2>
    <p class="block copy play-copy">Children can play together in a safe, clean and fun environment no matter what the weather. Somewhere they can have fun expressing themselves in a creative and playful manner.</p>

    <h2 class="block section-title ice-title">ICE SKATING</h2>
    <h3 class="block subtitle ice-sub">(Age 5)</h3>
    <p class="block copy ice-copy">Come and see our Brand new huge 12M x 8M ice skating rink Suitable for ages 5 and over Its only £3 to skate for 30 Minutes we also have Penguins to help the little ones skate and have lots of fun call us today for more information.</p>

    <h2 class="block section-title juniors-title">FOR THE JUNIORS</h2>
    <h3 class="block subtitle juniors-sub">recommended for ages up to 12 years</h3>
    <p class="block copy juniors-copy">6m Drop slide, 4 Lane Astra Slide, Giant Spiral Slide, Wavy Slide, Climbing Wall, Double Sky Glide, Ball Cannon Arena, large separate Sports Area with interactive sports walls, and many more exciting and challenging features.</p>

    <h2 class="block section-title toddlers-title">FOR THE TODDLERS</h2>
    <h3 class="block subtitle toddlers-sub">recommended for ages up to 5 years</h3>
    <p class="block copy toddlers-copy">Giant Interactive Ball Pool with juggler, lifter &amp; shower, Wavy Slide, Tube Slide, climbing and obstacle features.</p>

    <h2 class="block section-title babies-title">FOR THE BABIES</h2>
    <h3 class="block subtitle babies-sub">recommended for ages up to 3 years</h3>
    <p class="block copy babies-copy">Soft Play Centre including shapes, puzzles, rockers and games, interactive panels.</p>
  </section>

  <section class="panel panel--parties">
    <h1 class="block panel-title parties-title">PARTIES</h1>
    <h2 class="block subtitle subtitle--center parties-sub">Celebrate your big day with us</h2>

    <h2 class="block section-title football-title">FOOTBALL PARTY</h2>
    <h3 class="block subtitle football-sub">In our enclosed pitch</h3>
    <p class="block copy football-copy">Taken by a professional football coach, the children will receive some training and then get to play a game. The birthday child will also receive a leather football to take away! There will also be time for a play in the play area and you'll get your own party room for the party food and cake!</p>

    <h2 class="block section-title bumper-title">BUMPER CAR PARTY</h2>
    <h3 class="block subtitle bumper-sub">NEW for 2016 – launching spring</h3>
    <p class="block copy bumper-copy">Book a Kids Bumper Car party and get 30 minutes exclusive use of the bumper cars! The children will also get an hours play and half hour in their own party room for food and the cake celebration! (cake not included).</p>

    <p class="block copy contact-copy">hopscotchburrow.com<br>facebook.com/hopscotchburrow</p>
  </section>
</main>
</body>
</html>
```